Stationery Design Project

We are a start up wine business based in Sydney Australia. We already have a logo and are in the process of completing our website. We require our logo to be cleverly and artfully incorporated into our stationary requirements. Which will initially begin with a company letter head.
As we desire consistency across our brand, we will also be wanting to develop banner advertisements and brochure with the same "look".
If outstanding we move design brief to banner advertisement for web and banner of the website itself.
Older wealthy predominantly male demographic
Business

```html
<!DOCTYPE html>
<html lang="en">
<head>
<meta charset="utf-8">
<title>Heritage Vine Trading – Business Card</title>
<link rel="stylesheet" href="https://fonts.googleapis.com/css2?family=Arimo:wght@400&display=swap">
<style>
  :root {
    --page-bg: #d9dee1;
    --card-dark: #2f2d2e;
    --card-dark-deco: #272526;
    --card-light: #ffffff;
    --card-light-deco: #f2f2f2;
    --ink: #1c1c1c;
    --crimson: #b3123f;
    --logo-grey: #5b5b5b;
  }
  * { margin: 0; padding: 0; box-sizing: border-box; }
  html, body {
    width: 1200px; height: 960px; overflow: hidden;
    background: var(--page-bg);
    font-family: "Arimo", Arial, sans-serif;
  }
  .canvas {
    width: 1200px; height: 960px;
    display: flex; flex-direction: column;
    align-items: center; justify-content: center; gap: 60px;
  }
  .card {
    position: relative; width: 640px; height: 366px; overflow: hidden;
    box-shadow: 0 6px 18px rgba(0,0,0,.18);
  }
  .card--front { background: var(--card-dark); }
  .card--back { background: var(--card-light); }
  .monogram-area {
    position: absolute; border-radius: 48% 52% 45% 55%;
  }
  .card--front .monogram-area {
    left: 30px; top: 10px; width: 400px; height: 340px;
    background: var(--card-dark-deco);
  }
  .card--back .monogram-area {
    left: 250px; top: 10px; width: 360px; height: 330px;
    background: var(--card-light-deco);
  }
  .brand {
    position: absolute; display: flex; align-items: center; gap: 10px;
    font-size: 22px; font-weight: 400; line-height: 1.15;
  }
  .brand__dot { width: 14px; height: 14px; border-radius: 50%; flex: none; }
  .card--front .brand { right: 30px; top: 160px; color: var(--crimson); }
  .card--front .brand__dot { background: var(--crimson); }
  .card--back .brand { right: 34px; top: 168px; color: var(--logo-grey); }
  .card--back .brand__dot { background: var(--logo-grey); }
  .contact {
    position: relative; padding: 40px 0 0 40px; color: var(--ink);
  }
  .contact__name, .contact__role { font-size: 24px; line-height: 1.2; }
  .contact__details {
    margin-top: 26px; font-size: 16px; line-height: 1.3; list-style: none;
  }
  .contact__web { color: var(--crimson); }
</style>
</head>
<body>
<main class="canvas">
  <section class="card card--front">
    <div class="monogram-area" role="img" aria-label="Large faint script initial decoration"></div>
    <div class="brand"><span class="brand__dot"></span><span>Heritage Vine<br>Trading</span></div>
  </section>

  <section class="card card--back">
    <div class="monogram-area" role="img" aria-label="Large faint script initial decoration"></div>
    <div class="contact">
      <p class="contact__name">Clara Hendricks</p>
      <p class="contact__role">Director</p>
      <ul class="contact__details">
        <li>PO Box 418</li>
        <li>Kellerton NSW 2047</li>
        <li>t:&nbsp; 0491570156</li>
        <li>e: clara@heritagevine.com.au</li>
        <li class="contact__web">www.heritagevine.com.au</li>
      </ul>
    </div>
    <div class="brand"><span class="brand__dot"></span><span>Heritage Vine<br>Trading</span></div>
  </section>
</main>
</body>
</html>
```